Rw building ventures pty ltd

This is a development and construction company. Website can be set up on our domain rwbuildworks.net if we could change the domain to rwbuildworks.com.au would be great

Want the page to have eye catching designs, red, black and white are the preffered colours.

Check out www.toluqin.com.au it is my former company with my partner which i am now venturing out on my own, that is the perfect example of the website i want even allot of the information would be the same

Industry/Entity Type

Construction

Coding

Coded - Design and coding required

Number of Pages Required

5+ page

Requirements
Must have
• Company logo eye catching designs

```html
<!DOCTYPE html>
<html lang="en">
<head>
<meta charset="utf-8">
<title>RW Buildworks — Construction Services</title>
<link href="https://fonts.googleapis.com/css2?family=Nunito:wght@700;800;900&family=Lato:wght@400;700&display=swap" rel="stylesheet">
<style>
:root{
  --red:#e63a1f;
  --black:#1d1d1d;
  --ink:#222;
  --grey:#555;
  --line:#8a8a8a;
  --white:#fff;
  --pale:#ececec;
}
*{box-sizing:border-box;margin:0;padding:0}
html,body{width:1200px;height:3987px;overflow:hidden;background:var(--white)}
body{position:relative;font-family:'Lato',sans-serif;color:var(--ink)}
.abs{position:absolute}
.head{font-family:'Nunito',sans-serif;font-weight:900}
.brand{font-family:'Nunito',sans-serif;font-weight:800;letter-spacing:2px;color:var(--white);white-space:nowrap}

/* hero */
.hero{left:0;top:0;width:1200px;height:640px;background:linear-gradient(180deg,#7f8a93 0%,#4a4d52 45%,#2b2a2c 100%)}
.phone-pill{left:797px;top:8px;width:163px;height:38px;border-radius:19px;background:var(--red);color:#fff;font:700 14px 'Lato',sans-serif;display:flex;align-items:center;padding-left:8px;gap:8px}
.phone-pill .dot{width:28px;height:28px;border-radius:50%;background:#fff;display:flex;align-items:center;justify-content:center}
.social{width:30px;height:30px;border-radius:50%;background:#fff}
.nav{left:472px;top:62px;width:728px;height:46px;background:#151515;display:flex;align-items:center}
.nav a{color:#fff;text-decoration:none;font:700 15px 'Lato',sans-serif;letter-spacing:.5px;padding:0 29px;height:46px;display:flex;align-items:center}
.nav a.active{background:var(--red);clip-path:polygon(16px 0,100% 0,100% 100%,0 100%);padding-left:48px;padding-right:42px}
.hero-title{left:0;width:1200px;top:212px;text-align:center;color:#fff;font-size:64px;line-height:80px;letter-spacing:1px;text-shadow:0 2px 6px rgba(0,0,0,.35)}
.btn-red{background:var(--red);color:#fff;border-radius:22px;font:800 15px 'Nunito',sans-serif;display:flex;align-items:center;justify-content:space-between;padding:0 6px 0 20px}
.btn-red .ic{width:30px;height:30px;border-radius:50%;background:#fff;display:flex;align-items:center;justify-content:center}
.arrow{width:32px;height:32px;border-radius:50%;border:2px solid rgba(255,255,255,.85);display:flex;align-items:center;justify-content:center}

/* about */
.kicker{color:var(--red);font-family:'Nunito',sans-serif;font-weight:700;font-size:36px;letter-spacing:1px}
.title{font-family:'Nunito',sans-serif;font-weight:900;font-size:40px;color:var(--ink);letter-spacing:1px}
.rule{height:1px;background:var(--line)}
.about-sub{left:70px;top:735px;font:700 14px 'Lato',sans-serif}
.about-text{left:72px;top:775px;width:525px;font-size:15px;line-height:25.5px;color:#333}
.btn-outline{left:73px;top:957px;width:152px;height:40px;border:2px solid #333;border-radius:20px;display:flex;align-items:center;justify-content:space-between;padding:0 3px 0 17px;font:800 14px 'Nunito',sans-serif}
.btn-outline .ic{width:30px;height:30px;border-radius:50%;background:var(--red)}
.about-photo{left:619px;top:763px;width:504px;height:244px;border-radius:120px 30px 30px 120px;background:linear-gradient(135deg,#8fb0d2 0%,#cfd6dd 40%,#6b5148 70%,#2c2c30 100%)}

/* services */
.services{left:0;top:1102px;width:1200px;height:636px;background:var(--black)}
.services h2{position:absolute;top:52px;width:100%;text-align:center;color:#fff;font-size:40px;letter-spacing:1px}
.svc-name{color:#fff;font:700 18px 'Nunito',sans-serif}
.svc-text{color:#e4e4e4;font-size:15px;line-height:23px}
.r{text-align:right}
.centre-label{left:420px;top:1456px;width:360px;text-align:center;font-size:27px;letter-spacing:1.5px}

/* projects */
.proj{background:linear-gradient(180deg,#8db2d8 0%,#c6d2dc 45%,#5b5d60 75%,#8a8f89 100%)}

/* testimonials */
.testi{left:0;top:2585px;width:1200px;height:441px;background:linear-gradient(180deg,#e3e3e3,#d6d6d6)}
.testi h2{position:absolute;top:60px;width:100%;text-align:center;font-size:40px;letter-spacing:1px}
.quote{left:255px;top:2751px;width:690px;text-align:center;font-size:15px;line-height:27px;color:#333}
.q{color:var(--red);font:900 34px 'Nunito',sans-serif;line-height:0;vertical-align:-10px}
.avatar{left:540px;top:2903px;width:68px;height:68px;border-radius:50%;background:linear-gradient(180deg,#6a5a52,#2b2523);border:3px solid #fff}
.arrow-dark{border-color:#555}

/* contact form */
.field{border:1px solid #777;background:#fff;font-size:12.5px;color:#333;padding:14px 12px}
.home-photo{left:704px;top:3099px;width:420px;height:462px;background:linear-gradient(160deg,#e8e0cf 0%,#b49b7d 45%,#6e5c4c 100%);clip-path:polygon(0 0,100% 0,100% 100%,0 78%);box-shadow:0 4px 10px rgba(0,0,0,.3)}

/* footer */
.foot-h{color:#fff;font:700 16px 'Lato',sans-serif;letter-spacing:.5px}
.foot-h::after{content:"";display:block;width:88px;height:2px;background:var(--red);margin-top:10px}
.foot-link{color:#ddd;font-size:13px}
.foot-text{color:#ddd;font-size:12.5px;line-height:19px}
.vline{width:1px;background:#444;top:3640px;height:300px}
.ficon{width:26px;height:26px;border-radius:50%;background:var(--red);display:flex;align-items:center;justify-content:center}
.bottom-bar{left:0;top:3948px;width:1200px;height:39px;background:var(--red);color:#fff;font-size:12.5px}
</style>
</head>
<body>

<!-- HERO -->
<div class="abs hero" role="img" aria-label="Photo of a modern two-storey townhouse development with timber cladding under a grey sky"></div>
<svg class="abs" style="left:0;top:520px" width="1200" height="122" viewBox="0 0 1200 122">
  <polygon points="0,122 0,118 867,14 1200,112 1200,122" fill="#fff"/>
  <polyline points="0,114 867,2 1200,100" fill="none" stroke="#e63a1f" stroke-width="6"/>
</svg>
<div class="abs brand" style="left:70px;top:74px;font-size:26px">RW BUILDWORKS</div>
<div class="abs phone-pill"><span class="dot"><svg width="16" height="16" viewBox="0 0 24 24"><path d="M6.6 10.8a15 15 0 006.6 6.6l2.2-2.2c.3-.3.7-.4 1-.2 1.1.4 2.3.6 3.6.6.6 0 1 .4 1 1V20c0 .6-.4 1-1 1A17 17 0 013 4c0-.6.4-1 1-1h3.5c.6 0 1 .4 1 1 0 1.3.2 2.5.6 3.6.1.3 0 .7-.2 1z" fill="#e63a1f"/></svg></span>555 - 010 - 010</div>
<div class="abs social" style="left:979px;top:12px"></div>
<div class="abs social" style="left:1017px;top:12px"></div>
<div class="abs social" style="left:1055px;top:12px"></div>
<div class="abs social" style="left:1094px;top:12px"></div>
<nav class="abs nav">
  <a class="active">HOME</a><a>ABOUT US</a><a>SERVICES</a><a>PROJECTS</a><a>CONTACT US</a>
</nav>
<h1 class="abs hero-title head">WE PROVIDE<br>CONSTRUCTION SERVICE</h1>
<div class="abs btn-red" style="left:514px;top:410px;width:170px;height:40px">GET A QUOTE <span class="ic"><svg width="16" height="12" viewBox="0 0 16 12"><rect x="1" y="1" width="14" height="10" fill="none" stroke="#e63a1f" stroke-width="1.6"/><polyline points="1,1 8,7 15,1" fill="none" stroke="#e63a1f" stroke-width="1.6"/></svg></span></div>
<div class="abs arrow" style="left:72px;top:319px"><svg width="10" height="14"><polyline points="8,1 2,7 8,13" fill="none" stroke="#fff" stroke-width="2"/></svg></div>
<div class="abs arrow" style="left:1092px;top:319px"><svg width="10" height="14"><polyline points="2,1 8,7 2,13" fill="none" stroke="#fff" stroke-width="2"/></svg></div>

<!-- ABOUT -->
<div class="abs kicker" style="left:625px;top:632px">ABOUT</div>
<div class="abs title" style="left:625px;top:677px">RW BUILDWORKS</div>
<div class="abs rule" style="left:70px;top:689px;width:541px"></div>
<div class="abs about-sub">The Perfect Combination Of Innovation &amp; Quality for build your home</div>
<p class="abs about-text">It is a long established fact that a reader will be distracted by the readable content of a page when looking at its layout. The point of using Lorem Ipsum is that it has a more-or-less normal distribution of letters, as opposed to using 'Content here, content here', making it look like readable English. Many desktop publishing packages and web page editors now use Lorem Ipsum as their default model text,</p>
<div class="abs btn-outline">READ MORE <span class="ic"></span></div>
<div class="abs about-photo" role="img" aria-label="Photo of a finished townhouse facade seen through a large decorative frame"></div>

<!-- WHAT WE DO -->
<section class="abs services">
  <h2 class="head">WHAT WE DO</h2>
</section>
<svg class="abs" style="left:380px;top:1258px" width="440" height="440" viewBox="0 0 440 440">
  <circle cx="220" cy="220" r="197" fill="none" stroke="#fff" stroke-width="4"/>
</svg>
<div class="abs brand centre-label">RW BUILDWORKS.</div>
<svg class="abs" style="left:0;top:0" width="1200" height="1738" viewBox="0 0 1200 1738">
  <g fill="#e63a1f">
    <circle cx="471" cy="1310" r="37"/><circle cx="726" cy="1310" r="37"/>
    <circle cx="402" cy="1472" r="37"/><circle cx="797" cy="1472" r="37"/>
    <circle cx="472" cy="1636" r="37"/><circle cx="728" cy="1636" r="37"/>
  </g>
  <g fill="none" stroke="#fff" stroke-width="2">
    <rect x="458" y="1294" width="26" height="32" rx="2"/><line x1="463" y1="1303" x2="479" y2="1303"/><line x1="463" y1="1310" x2="479" y2="1310"/><line x1="463" y1="1317" x2="479" y2="1317"/>
    <circle cx="726" cy="1305" r="11"/><line x1="721" y1="1321" x2="731" y2="1321"/><line x1="722" y1="1326" x2="730" y2="1326"/>
    <path d="M392 1486v-16l6-8 4 6 4-8 4 10v16z"/>
    <circle cx="797" cy="1470" r="13"/><circle cx="797" cy="1470" r="7"/><circle cx="797" cy="1470" r="2"/>
    <circle cx="464" cy="1627" r="5"/><circle cx="480" cy="1627" r="5"/><path d="M455 1648c2-8 16-8 17-2 1-6 15-6 17 2"/>
    <rect x="713" y="1624" width="30" height="22" rx="2"/><circle cx="728" cy="1637" r="5"/>
  </g>
</svg>
<div class="abs svc-name r" style="left:218px;top:1270px;width:200px">Accountability</div>
<div class="abs svc-text r" style="left:158px;top:1307px;width:260px">Lorem Ipsum generators on the<br>Internet tend to repeat</div>
<div class="abs svc-name" style="left:810px;top:1270px">Transparency</div>
<div class="abs svc-text" style="left:814px;top:1309px">Lorem Ipsum generators on the<br>Internet tend to repeat</div>
<div class="abs svc-name r" style="left:148px;top:1430px;width:200px">Leadership</div>
<div class="abs svc-text r" style="left:88px;top:1468px;width:260px">Lorem Ipsum generators on the<br>Internet tend to repeat</div>
<div class="abs svc-name" style="left:858px;top:1431px">Strategic</div>
<div class="abs svc-text" style="left:858px;top:1470px">Lorem Ipsum generators on the<br>Internet tend to repeat</div>
<div class="abs svc-name r" style="left:220px;top:1596px;width:200px">Client Service</div>
<div class="abs svc-text r" style="left:160px;top:1634px;width:260px">Lorem Ipsum generators on the<br>Internet tend to repeat</div>
<div class="abs svc-name" style="left:791px;top:1597px">Integrity</div>
<div class="abs svc-text" style="left:792px;top:1636px">Lorem Ipsum generators on the<br>Internet tend to repeat</div>

<!-- RECENT PROJECTS -->
<div class="abs kicker" style="left:72px;top:1796px">OUR</div>
<div class="abs title" style="left:72px;top:1842px">RECENT PROJECTS</div>
<div class="abs rule" style="left:591px;top:1862px;width:536px"></div>
<div class="abs proj" style="left:71px;top:1937px;width:260px;height:284px" role="img" aria-label="Photo of a narrow grey two-storey home with glass entry"></div>
<div class="abs proj" style="left:348px;top:1937px;width:502px;height:284px" role="img" aria-label="Photo of a row of timber-clad townhouses with garages"></div>
<div class="abs proj" style="left:865px;top:1937px;width:262px;height:284px" role="img" aria-label="Photo of a white and charcoal modern residence"></div>
<div class="abs proj" style="left:71px;top:2232px;width:522px;height:285px" role="img" aria-label="Photo of curved-roof townhouses with brick base and timber battens"></div>
<div class="abs proj" style="left:607px;top:2232px;width:520px;height:285px" role="img" aria-label="Photo of a white rendered contemporary home with timber garage door"></div>

<!-- TESTIMONIALS -->
<section class="abs testi" role="img" aria-label="Faint background photo of a modern home facade">
  <h2 class="head">TESTIMONIALS</h2>
</section>
<p class="abs quote"><span class="q">“</span> It is a long established fact that a reader will be distracted by the readable content of a page when looking at its layout. The point of using Lorem Ipsum is that it has a more-or-less normal distribution of letters, as opposed to using 'Content here, content here', making it look like readable English. Many desktop publishing packages and web page editors now use Lorem Ipsum as their default model text. <span class="q">”</span></p>
<div class="abs avatar" role="img" aria-label="Client portrait"></div>
<div class="abs" style="left:625px;top:2912px;font:700 19px 'Nunito',sans-serif">SAM ORTELL</div>
<div class="abs" style="left:625px;top:2943px;font-size:13px;color:#555;letter-spacing:.5px">NEWYORK</div>
<div class="abs arrow arrow-dark" style="left:72px;top:2791px"><svg width="10" height="14"><polyline points="8,1 2,7 8,13" fill="none" stroke="#555" stroke-width="2"/></svg></div>
<div class="abs arrow arrow-dark" style="left:1092px;top:2791px"><svg width="10" height="14"><polyline points="2,1 8,7 2,13" fill="none" stroke="#333" stroke-width="2"/></svg></div>

<!-- CONTACT FORM -->
<div class="abs kicker" style="left:69px;top:3085px">LET'S BUILD</div>
<div class="abs title" style="left:69px;top:3131px">HOME TOGETHER</div>
<div class="abs field" style="left:71px;top:3211px;width:267px;height:50px">First Name :</div>
<div class="abs field" style="left:350px;top:3211px;width:267px;height:50px">Last Name :</div>
<div class="abs field" style="left:71px;top:3271px;width:267px;height:49px">Phone :</div>
<div class="abs field" style="left:350px;top:3271px;width:267px;height:49px">Email :</div>
<div class="abs field" style="left:71px;top:3333px;width:546px;height:125px">Message :</div>
<div class="abs btn-red" style="left:71px;top:3471px;width:162px;height:41px">SUBMIT NOW <span class="ic"><svg width="14" height="14" viewBox="0 0 14 14"><polyline points="3,7 7,3 11,7" fill="none" stroke="#333" stroke-width="1.6"/><line x1="7" y1="3" x2="7" y2="12" stroke="#333" stroke-width="1.6"/></svg></span></div>
<div class="abs home-photo" role="img" aria-label="Photo of a happy couple sitting on the stairs of their new home with a tablet"></div>

<!-- FOOTER -->
<svg class="abs" style="left:0;top:3470px" width="1200" height="480" viewBox="0 0 1200 480">
  <polygon points="0,160 786,14 1200,144 1200,480 0,480" fill="#1d1d1d"/>
  <polyline points="0,152 786,6 1200,136" fill="none" stroke="#e63a1f" stroke-width="5"/>
</svg>
<div class="abs vline" style="left:289px"></div>
<div class="abs vline" style="left:537px"></div>
<div class="abs vline" style="left:785px"></div>
<div class="abs brand" style="left:70px;top:3712px;font-size:22px">RW BUILDWORKS.</div>
<div class="abs social" style="left:74px;top:3810px;width:32px;height:32px"></div>
<div class="abs social" style="left:116px;top:3810px;width:32px;height:32px"></div>
<div class="abs social" style="left:157px;top:3810px;width:32px;height:32px"></div>
<div class="abs social" style="left:199px;top:3810px;width:32px;height:32px"></div>

<div class="abs foot-h" style="left:361px;top:3670px">QUICK LINKS</div>
<div class="abs foot-link" style="left:361px;top:3727px">Home</div>
<div class="abs foot-link" style="left:361px;top:3755px">About</div>
<div class="abs foot-link" style="left:361px;top:3783px">Services</div>
<div class="abs foot-link" style="left:361px;top:3811px">Projects</div>
<div class="abs foot-link" style="left:361px;top:3838px">Contact</div>

<div class="abs foot-h" style="left:573px;top:3670px">CONTACT US</div>
<div class="abs ficon" style="left:573px;top:3733px"><svg width="12" height="16" viewBox="0 0 12 16"><path d="M6 0a6 6 0 00-6 6c0 4.5 6 10 6 10s6-5.5 6-10a6 6 0 00-6-6z" fill="#fff"/><circle cx="6" cy="6" r="2.2" fill="#e63a1f"/></svg></div>
<div class="abs foot-text" style="left:621px;top:3726px">Unit 14<br>Harbour Works,<br>72 Kestrel Lane</div>
<div class="abs ficon" style="left:573px;top:3788px"><svg width="13" height="13" viewBox="0 0 24 24"><path d="M6.6 10.8a15 15 0 006.6 6.6l2.2-2.2c.3-.3.7-.4 1-.2 1.1.4 2.3.6 3.6.6.6 0 1 .4 1 1V20c0 .6-.4 1-1 1A17 17 0 013 4c0-.6.4-1 1-1h3.5c.6 0 1 .4 1 1 0 1.3.2 2.5.6 3.6.1.3 0 .7-.2 1z" fill="#fff"/></svg></div>
<div class="abs foot-text" style="left:621px;top:3792px">555-014-0288</div>
<div class="abs ficon" style="left:573px;top:3828px"><svg width="13" height="10" viewBox="0 0 16 12"><rect x="1" y="1" width="14" height="10" fill="#fff"/><polyline points="1,1 8,7 15,1" fill="none" stroke="#e63a1f" stroke-width="1.5"/></svg></div>
<div class="abs foot-text" style="left:621px;top:3832px">hello@rwbuildworks.com.au</div>

<div class="abs foot-h" style="left:827px;top:3670px">EMAIL SIGN UP</div>
<div class="abs field" style="left:827px;top:3732px;width:300px;height:45px;border:none;font-size:12.5px;padding:14px 20px">Email Address</div>
<div class="abs" style="left:825px;top:3786px;width:40px;height:40px;border-radius:50%;background:var(--red);display:flex;align-items:center;justify-content:center"><svg width="18" height="18" viewBox="0 0 24 24"><path d="M2 21l21-9L2 3v7l15 2-15 2z" fill="#fff"/></svg></div>
<div class="abs" style="left:878px;top:3796px;color:#fff;font:700 15px 'Lato',sans-serif;text-decoration:underline">SUBMIT NOW</div>

<div class="abs bottom-bar">
  <span class="abs" style="left:72px;top:12px">© 2021<b>RWBUILDWORKS</b> All rights reserved.</span>
  <span class="abs" style="left:864px;top:12px">Site Map &nbsp; | &nbsp; Terms Of Use &nbsp; | &nbsp; Privacy Policy</span>
</div>

</body>
</html>
```